Breast Cancer Car Donation Website Design

Please create a new one page website design.

Current site: http://www.givemyautohope.com/

The NEW website address will be RidesforPinkRibbonAid.org

Use these sites for an idea of what I am looking for. I like these sites best: drivesforheroesfund.org and autosforservicemen.org

```html
<!DOCTYPE html>
<html lang="en">
<head>
<meta charset="utf-8">
<title>Rides for Pink Ribbon Aid – One Page Site</title>
<link href="https://fonts.googleapis.com/css2?family=Roboto:wght@400;500;700;900&display=swap" rel="stylesheet">
<style>
:root{
  --backdrop:#262626;
  --pink:#e0157a;
  --pink-soft:#e39bb9;
  --pink-mid:#e56fa3;
  --ink:#222;
  --muted:#777;
  --panel:#f1f1f1;
  --black:#0b0b0b;
  --field:#5b5b5b;
  --white:#fff;
}
*{box-sizing:border-box;margin:0;padding:0}
html,body{width:1200px;height:1200px;overflow:hidden;background:var(--backdrop);font-family:'Roboto',sans-serif;color:var(--ink)}
.page{position:absolute;left:468px;top:0;width:265px;height:1200px;background:var(--white);overflow:hidden}
.abs{position:absolute}
.fill{position:absolute}
p{line-height:1.35}

/* hero */
.hero-photo{left:0;top:0;width:132px;height:136px;background:radial-gradient(circle at 70% 80%,#4a3a44 0,#1d1f2e 55%,#121424 100%)}
.hero-title{left:0;top:38px;width:132px;text-align:center;color:var(--white);font-weight:700;font-size:8.6px;line-height:10.5px;letter-spacing:.2px}
.hero-title span{color:var(--pink)}
.hero-copy{left:16px;top:74px;width:102px;text-align:center;color:#ddd;font-size:2.6px}
.feature{left:0;width:132px;display:flex;align-items:center;gap:6px;padding-left:17px;color:var(--white);font-size:4.6px;font-weight:500}
.feature svg{flex:none}
.f1{top:136px;height:30px;background:var(--pink-soft)}
.f2{top:166px;height:32px;background:var(--pink)}
.f3{top:198px;height:34px;background:var(--pink-soft)}
.form{left:132px;top:0;width:133px;height:232px;background:var(--black)}
.form .tab{position:absolute;left:4px;top:0;width:126px;height:9px;background:var(--pink);color:var(--white);font-size:3.6px;font-weight:700;text-align:center;line-height:9px}
.fld{position:absolute;width:52px;height:7px;background:var(--field);color:#ddd;font-size:2.4px;line-height:7px;padding-left:2px}
.form .note{position:absolute;left:10px;width:112px;text-align:center;color:#ccc;font-size:2.3px}
.form .rule{position:absolute;left:10px;width:113px;height:1px;background:#444}
.toggle-label{position:absolute;color:#ddd;font-size:2.4px;text-align:center}
.comments{position:absolute;left:10px;top:193px;width:113px;height:18px;background:var(--field);color:#ddd;font-size:2.4px;padding:2px}
.submit{position:absolute;left:53px;top:218px;width:52px;height:8px;background:var(--pink);color:var(--white);font-size:2.8px;font-weight:700;text-align:center;line-height:8px}

/* section titles */
.sec-title{left:0;width:265px;text-align:center;font-weight:700;font-size:6.2px;letter-spacing:.3px;color:var(--ink);line-height:8.5px}
.divider{width:24px;height:1px;background:var(--pink)}
.divider::after{content:"";position:absolute;left:10.5px;top:-1.5px;width:3px;height:3px;border-radius:50%;background:var(--pink)}

/* cards */
.card{top:269px;width:70px;height:99px;background:var(--white);box-shadow:0 1px 3px rgba(0,0,0,.25)}
.card .ph{position:absolute;left:0;top:0;width:70px;height:54px}
.card h4{position:absolute;top:58px;width:70px;text-align:center;font-size:3.2px;font-weight:700}
.card p{position:absolute;left:5px;top:64px;width:60px;text-align:center;font-size:2.3px;color:var(--muted)}
.card .more{position:absolute;top:91px;width:70px;text-align:center;font-size:2.3px;color:var(--pink);font-weight:700}

/* foundation */
.fdn-photo{left:0;top:384px;width:132px;height:138px;background:linear-gradient(135deg,#dfe3e8,#b9c1cb 55%,#e7eaee)}
.fdn-panel{left:132px;top:384px;width:133px;height:138px;background:var(--panel)}
.fdn-title{left:138px;top:399px;width:118px;font-size:5.2px;font-weight:700;line-height:7px}
.fdn-copy{left:138px;top:417px;width:120px;font-size:2.3px;color:var(--muted)}
.point{left:138px;width:122px;display:flex;gap:4px}
.point b{display:block;font-size:2.8px;margin-bottom:2px}
.point p{font-size:2.2px;color:var(--muted)}

/* help carousel */
.help{top:576px;height:98px;background:var(--pink);overflow:hidden}
.help .ph{position:absolute;left:0;top:0;width:100%;height:54px}
.help .bar{position:absolute;left:0;top:54px;width:100%;height:8px;background:#2a2a2a;color:var(--white);font-size:3px;font-weight:700;text-align:center;line-height:8px}
.help p{position:absolute;left:4px;right:4px;top:65px;color:var(--white);font-size:2.3px;text-align:center}
.help .more{position:absolute;left:0;width:100%;top:89px;text-align:center;color:var(--white);font-size:2.3px;font-weight:700}
.arrow{top:566px;width:7px;height:7px;background:var(--pink)}

/* gallery */
.gallery-bg{left:0;top:690px;width:265px;height:172px;background:var(--panel)}
.gal{width:74px;height:59px}

/* faq */
.q{height:7px;background:var(--pink);color:var(--white);font-size:2.4px;font-weight:700;line-height:7px;padding-left:5px}
.q.tall{height:11px;line-height:3.4px;padding-top:1px}
.ans{background:var(--panel)}
.ans p{font-size:2.2px;color:var(--muted);margin:0 4px 3px 8px}
.ans.list p{position:relative}
.ans.list p::before{content:"";position:absolute;left:-4px;top:.6px;width:2px;height:2px;border-radius:50%;background:var(--pink)}

/* contact */
.contact-bg{left:0;top:1026px;width:265px;height:136px;background:radial-gradient(circle at 35% 45%,#6e7a62,#3d4437 55%,#23261f)}
.phone-box{left:26px;top:1066px;width:104px;height:78px;background:rgba(230,140,180,.82);text-align:center;color:var(--white)}
.phone-box h3{margin-top:15px;font-size:8.4px;font-weight:700;letter-spacing:.4px}
.phone-box p{font-size:2.4px;margin:3px 12px 0}
.phone-box .num{font-size:6px;margin-top:3px}
.contact-box{left:141px;top:1042px;width:92px;height:104px;background:rgba(232,150,188,.88)}
.contact-head{position:absolute;left:0;top:0;width:92px;height:34px;background:var(--black);color:var(--white);text-align:center}
.contact-head h3{font-size:5.2px;font-weight:700;margin-top:8px}
.contact-head p{font-size:2.2px;margin:3px 5px 0;color:#ddd}
.cf{position:absolute;height:8px;border:.5px solid #f5c9dc;background:rgba(255,255,255,.12);color:var(--white);font-size:2.2px;line-height:7px;padding-left:2px}
.cf-btn{position:absolute;left:11px;top:91px;width:15px;height:6px;background:var(--white);color:var(--pink);font-size:2.2px;font-weight:700;text-align:center;line-height:6px}

/* footer */
.footer-title{left:0;top:1168px;width:265px;text-align:center;font-size:2.6px;font-weight:700}
.footer-copy{left:24px;top:1176px;width:217px;text-align:center;font-size:2.2px;color:var(--muted)}
.footer-bar{left:0;top:1192px;width:265px;height:8px;background:var(--pink);color:var(--white);font-size:2.2px;text-align:center;line-height:8px}
</style>
</head>
<body>
<main class="page">

  <!-- HERO -->
  <div class="fill hero-photo" role="img" aria-label="Hands holding a pink ribbon on a dark background"></div>
  <h1 class="abs hero-title">WELCOME TO <span>RIDES FOR<br>PINK RIBBON AID</span><br>ORGANIZATION</h1>
  <p class="abs hero-copy">Your car or boat donation helps support those affected by breast cancer and their families, with programs for screening, treatment and patient well-being. Our team is standing by 24 hours a day, 7 days a week to answer your questions and arrange your pickup quickly!</p>

  <div class="abs feature f1">
    <svg width="9" height="9" viewBox="0 0 10 10"><circle cx="5" cy="3" r="2" fill="#fff"/><path d="M1 10c0-3 2-4.5 4-4.5S9 7 9 10z" fill="#fff"/></svg>
    Fast Free Pickup - 24hr Response
  </div>
  <div class="abs feature f2">
    <svg width="10" height="9" viewBox="0 0 10 10"><path d="M1 8h8M2 8V5h2v3M5 8V3h2v5" stroke="#fff" stroke-width=".8" fill="none"/><path d="M2 3l6-2" stroke="#fff" stroke-width=".8"/></svg>
    Tax Deduction - Easy To Do!
  </div>
  <div class="abs feature f3">
    <svg width="9" height="10" viewBox="0 0 10 10"><path d="M5 1C2 3 3 6 1 9h2l2-4 2 4h2C7 6 8 3 5 1z" fill="#e0157a"/></svg>
    <span>Running or not - No Emission Test<br>Required</span>
  </div>

  <section class="fill form">
    <div class="tab">DONATION FORM</div>
    <div class="fld" style="left:10px;top:16px">First Name</div><div class="fld" style="left:71px;top:16px">Last Name</div>
    <div class="fld" style="left:10px;top:28px">Email</div><div class="fld" style="left:71px;top:28px">Day Phone</div>
    <div class="fld" style="left:10px;top:40px">Cell Phone</div><div class="fld" style="left:71px;top:40px">Evening Phone</div>
    <div class="fld" style="left:10px;top:52px">Street Name</div><div class="fld" style="left:71px;top:52px">City</div>
    <div class="fld" style="left:10px;top:64px">State</div><div class="fld" style="left:71px;top:64px">Zip</div>
    <p class="note" style="top:75px">If your vehicle is at a different location, please provide detailed information</p>
    <div class="fld" style="left:10px;top:84px">Pickup Street Name</div><div class="fld" style="left:71px;top:84px">Pickup City</div>
    <div class="fld" style="left:10px;top:96px">Pickup State</div><div class="fld" style="left:71px;top:96px">Pickup Zip</div>
    <div class="rule" style="top:106px"></div>
    <div class="fld" style="left:10px;top:112px">Vehicle Year</div><div class="fld" style="left:71px;top:112px">Vehicle Make</div>
    <div class="fld" style="left:10px;top:124px">Vehicle Model</div><div class="fld" style="left:71px;top:124px">Vehicle Color</div>
    <div class="fld" style="left:10px;top:136px">VIN (if available)</div><div class="fld" style="left:71px;top:136px">Mileage</div>
    <div class="toggle-label" style="left:20px;top:147px;width:40px">Major Body Damage:<br>Yes <svg width="7" height="3"><rect width="7" height="3" rx="1.5" fill="#fff"/></svg> No</div>
    <div class="toggle-label" style="left:72px;top:147px;width:40px">Do you have title<br>Yes <svg width="7" height="3"><rect width="7" height="3" rx="1.5" fill="#fff"/></svg> No</div>
    <div class="toggle-label" style="left:40px;top:161px;width:52px">Not Running <svg width="7" height="3"><rect width="7" height="3" rx="1.5" fill="#fff"/></svg> Running</div>
    <div class="rule" style="top:168px"></div>
    <p class="note" style="top:173px">We accept cars with no title and/or in poor condition, but we may choose to send them to a different partner for pickup. Any information you can provide helps us decide. Mileage or repairs may be considered. Please call us to learn more.</p>
    <div class="comments">Comments</div>
    <div class="submit">SUBMIT</div>
  </section>

  <!-- ABOUT BREAST CANCER -->
  <h2 class="abs sec-title" style="top:248px">ABOUT BREAST CANCER</h2>
  <div class="abs divider" style="left:120px;top:259px"></div>

  <article class="abs card" style="left:23px">
    <div class="ph" role="img" aria-label="Medical team with imaging equipment" style="background:linear-gradient(135deg,#b9cddd,#6f8aa3)"></div>
    <h4>WHAT IS CANCER</h4>
    <p>Cancer is a group of many related diseases that begin in cells, the body's basic building blocks. To understand cancer, it is helpful to know what happens when normal cells.</p>
    <div class="more">READ MORE →</div>
  </article>
  <article class="abs card" style="left:98px">
    <div class="ph" role="img" aria-label="Scattered pills on a table" style="background:linear-gradient(135deg,#d9c4c6,#a58d90)"></div>
    <h4>SYMPTOMS &amp; RISK FACTORS</h4>
    <p>Cancer is the second leading cause of death in the country. However, improvements in cancer detection, diagnosis, and treatment have increased the survival rate.</p>
    <div class="more">READ MORE →</div>
  </article>
  <article class="abs card" style="left:173px">
    <div class="ph" role="img" aria-label="Researcher working in a laboratory" style="background:linear-gradient(135deg,#e0c9a6,#6d7fa3)"></div>
    <h4>WHAT CAUSES CANCER?</h4>
    <p>Scientists have learned that cancer is caused by changes called alterations in genes that control normal cell growth and cell death. Certain lifestyle factors can change.</p>
    <div class="more">READ MORE →</div>
  </article>

  <!-- FOUNDATION -->
  <div class="fill fdn-photo" role="img" aria-label="Desk seen from above with hands typing on a laptop"></div>
  <div class="fill fdn-panel"></div>
  <h2 class="abs fdn-title">ABOUT PINK RIBBON RELIEF ALLIANCE FOUNDATION</h2>
  <p class="abs fdn-copy">The Pink Ribbon Relief Alliance is committed to making a positive difference in the lives of those affected with breast cancer as well as those families affected by breast cancer. The Alliance financially supports a variety of programs dedicated to breast cancer screening and prevention, treatment and patient health and well-being.</p>
  <div class="abs point" style="top:441px">
    <svg width="9" height="9" viewBox="0 0 10 10"><circle cx="5" cy="3" r="2" fill="#e0157a"/><path d="M1 10c0-3 2-4.5 4-4.5S9 7 9 10z" fill="#e0157a"/></svg>
    <div><b>The Purpose</b><p>To make a positive difference in the lives of those afflicted with or affected by breast cancer.</p></div>
  </div>
  <div class="abs point" style="top:462px">
    <svg width="9" height="9" viewBox="0 0 10 10"><rect x="1" y="3" width="8" height="4" rx="2" fill="none" stroke="#e0157a" stroke-width="1"/></svg>
    <div><b>The Business</b><p>Providing grants to hospitals and community centers to benefit patients and families with breast cancer and helpful assistance and information to the current breast cancer patient.</p></div>
  </div>
  <div class="abs point" style="top:488px">
    <svg width="9" height="9" viewBox="0 0 10 10"><path d="M2 2l6 6M8 2L2 8" stroke="#e0157a" stroke-width="1.6"/></svg>
    <div><b>The Values</b><p>Easing the stress and strain that cancer can cause a patient and their families, health and wellness.</p></div>
  </div>

  <!-- HOW PRRA HELPS -->
  <h2 class="abs sec-title" style="top:538px">HOW DOES PRRA HELP IN THE FIGHT<br>AGAINST BREAST CANCER</h2>
  <div class="abs divider" style="left:120px;top:558px"></div>
  <div class="abs arrow" style="left:226px"><svg width="7" height="7"><path d="M4.3 2L2.7 3.5 4.3 5" stroke="#fff" stroke-width=".7" fill="none"/></svg></div>
  <div class="abs arrow" style="left:234px"><svg width="7" height="7"><path d="M2.7 2l1.6 1.5L2.7 5" stroke="#fff" stroke-width=".7" fill="none"/></svg></div>

  <article class="abs help" style="left:23px;width:33px">
    <div class="ph" role="img" aria-label="Library bookshelves" style="background:linear-gradient(135deg,#8a6a4a,#3e2e22)"></div>
    <div class="bar" style="text-align:left;padding-left:1px">FUNDS</div>
    <p style="left:1px;text-align:left">Scholarship fund for single parent homes, in treatment or recovery.</p>
    <div class="more" style="text-align:left">RE →</div>
  </article>
  <article class="abs help" style="left:60px;width:69px">
    <div class="ph" role="img" aria-label="Surgeon in scrubs in an operating room" style="background:linear-gradient(135deg,#9fc3d9,#4d7a9a)"></div>
    <div class="bar">RECONSTRUCTIVE SURGERY</div>
    <p>The Alliance has partnered with hospitals to be able to provide women with breast reconstructive surgery at little or no cost to them.</p>
    <div class="more">READ MORE →</div>
  </article>
  <article class="abs help" style="left:133px;width:69px">
    <div class="ph" role="img" aria-label="Hospital emergency entrance sign" style="background:linear-gradient(135deg,#c8474a,#7b3034)"></div>
    <div class="bar">CHILD SPONSORSHIP</div>
    <p>The Alliance is financially assisting children whose families have been directly affected by breast cancer. We currently support two young students in the U.S.</p>
    <div class="more">READ MORE →</div>
  </article>
  <article class="abs help" style="left:206px;width:36px">
    <div class="ph" role="img" aria-label="Patient receiving a vaccine" style="background:linear-gradient(135deg,#d8dde6,#8795ad)"></div>
    <div class="bar" style="text-align:right;padding-right:1px">HOLISTIC</div>
    <p style="right:1px">PRRA believes it is a crucial aid to treat only traditional medical cancer.</p>
    <div class="more" style="text-align:right">READ M</div>
  </article>

  <!-- GALLERY -->
  <div class="fill gallery-bg"></div>
  <h2 class="abs sec-title" style="top:706px">OUR GALLERY</h2>
  <div class="abs divider" style="left:120px;top:716px"></div>
  <div class="abs gal" style="left:21px;top:727px;background:linear-gradient(135deg,#8a5a3f,#b5432c 55%,#3b5358)" role="img" aria-label="Rusty red vintage car by a brick wall"></div>
  <div class="abs gal" style="left:96px;top:727px;background:linear-gradient(180deg,#2f8fb3,#9fc9d4 45%,#b07a54)" role="img" aria-label="Boat on a sandy beach"></div>
  <div class="abs gal" style="left:171px;top:727px;background:linear-gradient(180deg,#3d4f5e,#a8443b 55%,#e8e8e8)" role="img" aria-label="Red classic car on a tow trailer"></div>
  <div class="abs gal" style="left:21px;top:788px;background:linear-gradient(135deg,#6b7f8c,#4fa8cf 55%,#394b55)" role="img" aria-label="Light blue vintage compact car"></div>
  <div class="abs gal" style="left:96px;top:788px;background:linear-gradient(180deg,#1d3447,#d27a3a 55%,#152230)" role="img" aria-label="Boat on water at sunset"></div>
  <div class="abs gal" style="left:171px;top:788px;background:linear-gradient(135deg,#2a2a2a,#6d6d6d 55%,#1e1e1e)" role="img" aria-label="Black and white classic sedan in a garage"></div>

  <!-- FAQ -->
  <h2 class="abs sec-title" style="top:879px">FREQUENTLY ASKED QUESTIONS</h2>
  <div class="abs divider" style="left:120px;top:889px"></div>

  <div class="abs" style="left:23px;top:901px;width:107px">
    <div class="q">⊖ WHY DONATE A VEHICLE OR VESSEL?</div>
    <div class="ans list" style="padding:4px 0 1px">
      <p>Free pickup, whether the vehicle or vessel is running or not.</p>
      <p>No hassles! No calls, questions, or price haggling to sell your car or boat.</p>
      <p>No strangers coming to your home, no worries about liability, no emissions check required.</p>
      <p>No cost! You won't need to do minor repairs, pay for an ad or sell your item, or pay for an emissions check.</p>
      <p>Avoid confusing paperwork, title transfers, etc. Qualifies for IRS Tax Deduction.</p>
    </div>
    <div class="q" style="margin-top:6px">⊕ HOW DO I DONATE A VEHICLE OR VESSEL?</div>
    <div class="q tall" style="margin-top:3px">⊕ HOW DOES MY VEHICLE OR VESSEL DONATION BENEFIT THE<br>CHARITY?</div>
    <div class="q" style="margin-top:3px">⊕ HOW LONG DOES IT TAKE TO PICKUP MY DONATION?</div>
  </div>

  <div class="abs" style="left:136px;top:901px;width:106px">
    <div class="q tall">⊖ DO I HAVE ANY LIABILITY AFTER THE VEHICLE/VESSEL IS<br>PICKED UP?</div>
    <div class="ans" style="padding:4px 0 2px">
      <p style="margin-left:4px">The auction will transfer title to the buyer, who will then be responsible for any liability. Some states require that you file a notice (Release of Liability/Transfer of Ownership, etc.) with the state department that handles motor vehicles. We recommend that you file that form, in some states you are responsible to cancel the license plates and to notify your insurance company. We suggest you follow recommended procedures in your state.</p>
    </div>
    <div class="q" style="margin-top:3px">⊕ HOW DOES DONATING A CAR OR BOAT BENEFIT MY TAXES?</div>
    <div class="q" style="margin-top:3px">⊕ WHAT HAPPENS TO MY CAR AFTER IT'S PICKED UP?</div>
    <div class="q" style="margin-top:3px">⊕ WHAT KIND OF DONATIONS CAN THE CHARITY ACCEPT?</div>
  </div>

  <!-- CONTACT -->
  <div class="fill contact-bg" role="img" aria-label="Vintage green camper van parked in a field"></div>
  <div class="abs phone-box">
    <h3>DONATE BY PHONE</h3>
    <p>To make a donation by phone, call the Pink Ribbon Relief Alliance Donation Center at</p>
    <div class="num">800-555-0142</div>
  </div>
  <section class="abs contact-box">
    <div class="contact-head">
      <h3>Contact Us</h3>
      <p>For all other inquiries, please fill out the form below and include your name, phone number, email address (if you have one), and your question. We will respond to you shortly.</p>
    </div>
    <div class="cf" style="left:11px;top:42px;width:37px">First Name</div>
    <div class="cf" style="left:51px;top:42px;width:37px">Last Name</div>
    <div class="cf" style="left:11px;top:54px;width:37px">Phone no</div>
    <div class="cf" style="left:51px;top:54px;width:37px">Email</div>
    <div class="cf" style="left:11px;top:66px;width:77px;height:20px">Your Message</div>
    <div class="cf-btn">SUBMIT</div>
  </section>

  <!-- FOOTER -->
  <div class="abs footer-title">PRIVACY POLICY</div>
  <p class="abs footer-copy">Pink Ribbon Relief Alliance is a 501(c)(3) non-profit organization in full accordance with all laws and regulations of the US Government and the IRS. Your donation is tax-deductible in accordance with Federal regulations.</p>
  <div class="abs footer-bar">© Pink Ribbon Relief Alliance 2018. All Rights Reserved</div>
</main>
</body>
</html>
```